Business Card Design

This is a coaching and training company. We deliver personal development workshops, training and one to one coaching. We would like the current logo to be used.

Target Market(s)

For coaches, small business owners and people aged around 40-60 who are seeking direction in their life

Industry/Entity Type

Training

Contact Information for Business Card

Marion Tuckett
Speaker-Trainer-Coach
There is no going back ...
0461 738196
18 Harrow Lane Pembry
mtuckett47@quillbox.net

Font styles to use
Sans Serif

Requirements
Should not have
• No old style fonts

```html
<!DOCTYPE html>
<html lang="en">
<head>
<meta charset="utf-8">
<title>Tideford Business Card – Option 1</title>
<link href="https://fonts.googleapis.com/css2?family=Montserrat:ital,wght@0,300;0,400;1,300&display=swap" rel="stylesheet">
<style>
  :root {
    --board-grey: #bcbec0;
    --card-white: #ffffff;
    --ink: #231f20;
    --accent-blue: #29a9e0;
    --tagline-blue: #4fb3e3;
    --brand-blue: #2a9dd0;
    --mark-grey: #e4e5e6;
    --note-red: #ed1c24;
  }
  * { margin: 0; padding: 0; box-sizing: border-box; }
  html, body { width: 953px; height: 1200px; overflow: hidden; }
  body {
    background: var(--board-grey);
    font-family: "Montserrat", Arial, sans-serif;
    color: var(--ink);
    position: relative;
  }
  .card {
    position: absolute;
    left: 73px;
    width: 798px;
    height: 493px;
    background: var(--card-white);
  }
  .card--front { top: 68px; }
  .card--back { top: 581px; }

  .brand-square {
    position: absolute;
    left: 171px;
    top: 200px;
    width: 150px;
    height: 150px;
    background: var(--mark-grey);
  }
  .brand-name {
    position: absolute;
    left: 171px;
    top: 384px;
    font-size: 44px;
    font-weight: 400;
    letter-spacing: 2px;
    color: var(--brand-blue);
  }

  .contact {
    position: absolute;
    right: 30px;
    text-align: right;
    font-weight: 300;
    font-size: 20px;
    line-height: 1.3;
  }
  .contact--identity { top: 56px; }
  .contact__name { font-size: 22px; }
  .contact__role { color: var(--accent-blue); }
  .contact--details { top: 330px; }
  .contact__email { color: var(--accent-blue); margin-top: 22px; }

  .tagline {
    position: absolute;
    left: 153px;
    top: 225px;
    font-size: 37px;
    font-weight: 300;
    font-style: italic;
    color: var(--tagline-blue);
    letter-spacing: 0.5px;
  }

  .spec {
    position: absolute;
    left: 75px;
    top: 1106px;
    font-size: 29px;
    font-weight: 400;
    line-height: 1.3;
  }
  .bleed-note {
    position: absolute;
    left: 648px;
    top: 1086px;
    display: flex;
    align-items: flex-start;
    gap: 10px;
    color: var(--note-red);
    font-size: 28px;
    line-height: 1.1;
  }
  .bleed-note svg { margin-top: 10px; }
</style>
</head>
<body>
  <section class="card card--front">
    <div class="brand-square"></div>
    <div class="brand-name">TIDEFORD</div>

    <div class="contact contact--identity">
      <p class="contact__name">Marion Tuckett Speaker</p>
      <p class="contact__role">Trainer-Coach</p>
    </div>

    <div class="contact contact--details">
      <p class="contact__phone">0461 738196</p>
      <p class="contact__address">18 Harrow Lane Pembry</p>
      <p class="contact__email">mtuckett47@quillbox.net</p>
    </div>
  </section>

  <section class="card card--back">
    <p class="tagline">There is no going back ...</p>
  </section>

  <div class="spec">
    <p>Option 1</p>
    <p>SIZE: 94mm x 58mm</p>
  </div>

  <div class="bleed-note">
    <svg width="68" height="22" viewBox="0 0 68 22" aria-hidden="true">
      <path d="M10 3 A9 9 0 0 0 10 19" fill="none" stroke="var(--note-red)" stroke-width="2" stroke-dasharray="3 3"/>
      <line x1="6" y1="11" x2="66" y2="11" stroke="var(--note-red)" stroke-width="2" stroke-dasharray="5 4"/>
      <path d="M4 8 L1 11 L4 14" fill="none" stroke="var(--note-red)" stroke-width="2"/>
    </svg>
    <p>Purposeful<br>bleed</p>
  </div>
</body>
</html>
```